Building company buisness cards

We are looking for a sharp modern new look for our business cards.
We are a New Zealand based company that specialises in house and land packages.
We have attached a photo of the current logo and would like to see if it can be improved somehow if needed.
We are open to any colours but we have chosen green at this stage.
Feel free to change the font and make the logo smarter looking.
Play with the colours and see what looks best.

We want a card that looks so good know one will want to throw it away!

Target Market(s)

Home buyers

Industry/Entity Type

Building

Contact Information for Business Card

Dorian Keswick
0217392604
dkeswick@tidewellhomecraft.co.nz
tidewellhomecraft.co.nz

Font styles to use
Serif
Sans Serif

Colors

Designer to choose colors to be used in the design.

Requirements
Must have
• Logo and company name on one side, details on the other side
Nice to have
• Color codes for the original green are HEX #4a8028, RGB(74,128,40), CMYK(42,0,69,50)
• Round corners, Raised and/or spot UV

```html
<!DOCTYPE html>
<html lang="en">
<head>
<meta charset="utf-8">
<title>Tidewell Homecraft — Business Cards</title>
<link href="https://fonts.googleapis.com/css2?family=Nunito:wght@700;800&display=swap" rel="stylesheet">
<style>
  :root {
    --bg: #1f1f20;
    --card-dark: #1b1b1c;
    --card-light: #ffffff;
    --brand-green: #4a8028;
    --ink: #141414;
    --rule: #cfd8c8;
  }
  * { box-sizing: border-box; margin: 0; padding: 0; }
  html, body { width: 1200px; height: 900px; overflow: hidden; background: var(--bg); }
  body { font-family: "Nunito", "Helvetica Neue", Arial, sans-serif; position: relative; }

  .card {
    position: absolute;
    left: 250px;
    width: 700px;
    height: 400px;
    border-radius: 10px;
    overflow: hidden;
    box-shadow: 0 10px 30px rgba(0,0,0,0.45);
  }

  /* Front: brand side */
  .card--front { top: 40px; background: var(--card-dark); }
  .brand-wordmark {
    position: absolute;
    inset: 0;
    display: flex;
    flex-direction: column;
    align-items: center;
    justify-content: center;
    color: var(--brand-green);
    font-weight: 800;
    line-height: 1;
  }
  .brand-wordmark__top { font-size: 40px; letter-spacing: 1px; }
  .brand-wordmark__main { font-size: 58px; margin-top: 4px; }

  /* Back: contact side */
  .card--back { top: 470px; background: var(--card-light); }
  .card--back .brand-wordmark { inset: 0 0 200px 0; justify-content: flex-end; }
  .card--back .brand-wordmark__top { font-size: 30px; }
  .card--back .brand-wordmark__main { font-size: 44px; }
  .brand-rule {
    position: absolute;
    top: 216px;
    left: 310px;
    width: 80px;
    height: 1px;
    background: var(--rule);
  }

  .holder-name {
    position: absolute;
    left: 48px;
    top: 272px;
    font-size: 36px;
    font-weight: 700;
    color: var(--brand-green);
  }

  .contact-list {
    position: absolute;
    left: 350px;
    top: 252px;
    list-style: none;
    color: var(--ink);
    font-size: 17px;
    font-weight: 800;
  }
  .contact-list li { display: flex; align-items: center; gap: 10px; height: 30px; }
  .contact-list svg { width: 16px; height: 16px; flex: none; }

  .green-band {
    position: absolute;
    left: 0; right: 0; bottom: 0;
    height: 48px;
    background: var(--brand-green);
  }
</style>
</head>
<body>

  <section class="card card--front" aria-label="Card front">
    <div class="brand-wordmark">
      <span class="brand-wordmark__top">tidewell</span>
      <span class="brand-wordmark__main">homecraft.</span>
    </div>
  </section>

  <section class="card card--back" aria-label="Card back">
    <div class="brand-wordmark">
      <span class="brand-wordmark__top">tidewell</span>
      <span class="brand-wordmark__main">homecraft.</span>
    </div>
    <div class="brand-rule"></div>

    <p class="holder-name">Dorian Keswick</p>

    <ul class="contact-list">
      <li>
        <svg viewBox="0 0 16 16" aria-hidden="true"><path fill="#4a8028" d="M2 5c0-1.5 2.5-2.5 6-2.5S14 3.5 14 5v1.5h-3V5H5v1.5H2zM3 8h10l1 5H2z"/></svg>
        0217392604
      </li>
      <li>
        <svg viewBox="0 0 16 16" aria-hidden="true"><rect x="1" y="3" width="14" height="10" fill="#4a8028"/><path d="M1.5 3.5 8 9l6.5-5.5" fill="none" stroke="#fff" stroke-width="1.3"/></svg>
        dkeswick@tidewellhomecraft.co.nz
      </li>
      <li>
        <svg viewBox="0 0 16 16" aria-hidden="true"><g fill="none" stroke="#4a8028" stroke-width="1.2"><circle cx="8" cy="8" r="6.5"/><ellipse cx="8" cy="8" rx="2.8" ry="6.5"/><path d="M1.5 8h13M2.5 4.8h11M2.5 11.2h11"/></g></svg>
        tidewellhomecraft.co.nz
      </li>
    </ul>

    <div class="green-band"></div>
  </section>

</body>
</html>
```